COMPETITION TITLE:
Premium Skincare Packaging Design for Modern Hydration Beauty Brand
ABOUT THE PROJECT
We are developing a new skincare brand called VELORENA.
We are looking for a sophisticated and commercially strong packaging design direction for our initial skincare soft launch.
The brand positioning is:
* modern premium skincare
* hydration-focused
* wellness-oriented
* calming and elegant
* emotionally reassuring
* modern feminine skincare
* premium online beauty brand
The products are designed around hydration, skin comfort and modern skincare rituals.
The brand is inspired by modern hydration and skin wellness for people adapting between warmer and colder climates. The visual direction should therefore feel emotionally warm, comforting and restorative while remaining modern, refined and internationally premium rather than overtly cultural or decorative.
WHAT WE NEED
We are primarily seeking the VISUAL DIRECTION and PACKAGING IDENTITY for one hero product:
LIGHT MOISTURISING DAY CREAM
The winning visual direction will later be adapted across additional products within the range, including:
* Brightening Eye Cream
* Hydrating Mist / Toner
Therefore we are looking for a cohesive skincare brand identity system rather than unrelated individual designs.
IMPORTANT PACKAGING INFORMATION
The product packaging is:
* white plastic pump dispenser bottle
* transparent clear plastic lid
* outer cardboard carton/box
Bottle dimensions:
* diameter: 30mm
* total height including lid: 147mm
* bottle body height: approx. 120mm
* transparent lid height: approx. 27mm
Outer carton dimensions:
* height: 150mm
* width: 40mm x 35mm
IMPORTANT:
The packaging itself is minimalist and lightweight, therefore the LABEL DESIGN and OVERALL BRAND DIRECTION should visually elevate the product and make it feel:
* premium
* substantial
* calming
* elegant
* modern
* trustworthy
* emotionally warm
* intentional
The design should help the packaging feel significantly more premium than standard mass-market skincare.
FILES PROVIDED
We are providing:
* bottle label template
* outer box template
* logo/icon
* packaging dimensions
The supplied logo/icon should be retained conceptually, however designers may professionally refine and recreate/vectorise the artwork where required for packaging consistency and premium presentation.
At this stage we are NOT looking for final technical production artwork.
We are primarily looking for:
* visual direction
* typography
* colour palette
* premium skincare aesthetic
* realistic product mockups
IMPORTANT WEBSITE NOTE
A current website link may be provided for background information only.
Please DO NOT take heavy visual inspiration from the existing website design, as the website itself is expected to evolve in the future alongside the packaging direction.
The packaging design should therefore LEAD the future visual identity of the brand rather than follow the current website styling.
DESIGN STYLE
We are looking for:
* modern premium wellness skincare
* understated luxury
* elegant typography
* emotionally warm but clean branding
* hydration-focused beauty aesthetic
* premium online skincare look
The product should feel:
* calming when held
* emotionally reassuring rather than clinical
* modern wellness rather than minimalist pharmacy
* elegant but human rather than cold luxury
* comforting and restorative rather than cosmetic-only
Subtle texture, tonal layering and sophisticated visual depth are encouraged where appropriate.
Designers are encouraged to create a recognisable and distinctive visual identity rather than generic minimalist skincare packaging.
PLEASE AVOID
* gold luxury clichés
* ornate decorative themes
* floral overload
* influencer-style beauty branding
* overly clinical pharmacy aesthetics
* generic Canva-style layouts
* packaging that feels cold or sterile
STYLE REFERENCES
Please take inspiration from brands such as:
* Mirven
* Plume Beauty
* Coraval
* Beauty of Dallith
We particularly like:
* elegant spacing
* clean premium typography
* calm colour palettes
* subtle luxury
* modern hydration skincare aesthetics
COLOUR DIRECTION
Preferred tones include:
* warm ivory
* soft cream
* muted blush
* sand
* charcoal typography
* subtle deep plum accents
* restrained muted rose-gold accents
Please avoid:
* neon colours
* excessive metallic effects
* harsh black-and-white pharmacy styling
* very dark packaging
IMPORTANT DESIGN NOTE
The slim vertical packaging should feel intentionally elegant and premium rather than small or sample-sized.
The label design should visually elongate and elevate the packaging.
LOGO
An existing logo/icon is provided and should be retained and integrated into the design direction rather than completely redesigned.
DELIVERABLES
We are looking for:
* one fully developed hero product design
* realistic bottle + outer box mockups
* coordinated visual direction suitable for future product extensions
* typography and colour direction
* editable source files
The final approved visual system will later be adapted across additional products within the range.
BRAND NAME
VELORENA
OPTIONAL TAGLINE DIRECTION
Tideshift Balance Hydration
Updates
Thank you everyone for the submissions so far — there are some very strong directions emerging.
A few important thoughts as the project develops:
We are looking not only for attractive skincare labels, but for a distinctive and recognisable BRAND IDENTITY that could grow with the business over time across future packaging formats including larger cartons, jars and premium skincare packaging.
One area we would particularly encourage designers to explore further is refinement/elevation of the existing logo/icon. We would like to retain the core rose/circle concept, however subtle refinement, balance, geometry, typography pairing and premium presentation are encouraged where appropriate.
The strongest directions for us so far are those that feel:
* emotionally warm rather than clinical
* modern premium wellness rather than generic minimal skincare
* calming and reassuring when viewed or held
* elegant and distinctive rather than trend-driven
* premium without relying on gold luxury clichés
We are especially interested in designs that create a memorable visual identity system rather than simply placing text onto a white skincare bottle.
Subtle tonal layering, refined typography, understated sophistication and intelligent visual restraint are all encouraged.
Many thanks again and we are very excited to see the next round of directions develop.

```html
<!DOCTYPE html>
<html lang="en">
<head>
<meta charset="utf-8">
<title>VELORENA — Skincare Packaging Range</title>
<link href="https://fonts.googleapis.com/css2?family=Marcellus&family=Montserrat:wght@400;500&display=swap" rel="stylesheet">
<style>
  :root {
    --canvas: #efe6dc;
    --blush: #f7e7e3;
    --blush-deep: #f0d8d2;
    --rose: #b5624f;
    --rose-soft: #c98a7b;
    --rose-line: #d9aa9d;
    --illustration-a: #f3dcd5;
    --illustration-b: #e8c3b8;
  }
  * { box-sizing: border-box; margin: 0; padding: 0; }
  html, body { width: 1200px; height: 800px; overflow: hidden; }
  body {
    background: var(--canvas);
    font-family: "Montserrat", sans-serif;
    color: var(--rose);
  }
  .range {
    width: 1200px; height: 800px;
    padding: 0 20px 70px;
    display: flex; align-items: flex-end; justify-content: space-between;
  }
  .label {
    background: var(--blush);
    display: flex; flex-direction: column; align-items: center;
    text-align: center;
    padding: 22px 10px 16px;
    box-shadow: 0 1px 0 rgba(181, 98, 79, 0.08);
  }
  .brand-mark {
    width: 30px; height: 30px;
    border: 1px solid var(--rose-soft);
    border-radius: 50%;
    margin-bottom: 8px;
  }
  .brand-name {
    font-family: "Marcellus", serif;
    font-size: 19px; letter-spacing: 1.5px;
    color: var(--rose);
    white-space: nowrap;
  }
  .brand-tagline {
    font-size: 6px; letter-spacing: 1.6px;
    color: var(--rose); margin-top: 3px;
    white-space: nowrap;
  }
  .product-name {
    font-family: "Marcellus", serif;
    font-size: 12px; letter-spacing: 1.6px; line-height: 1.45;
    color: var(--rose-soft); margin-top: 26px;
    text-transform: uppercase;
  }
  .product-benefit {
    font-size: 6.5px; letter-spacing: 0.6px; line-height: 1.5;
    color: var(--rose); margin-top: 5px; text-transform: uppercase;
  }
  .divider { width: 34px; height: 1px; background: var(--rose-line); margin: 10px 0; }
  .product-claim {
    font-size: 7px; letter-spacing: 0.8px; line-height: 1.5;
    color: var(--rose-soft); text-transform: uppercase;
  }
  .skin-type {
    font-size: 6px; letter-spacing: 0.8px;
    color: var(--rose); margin-top: 16px; text-transform: uppercase;
  }
  .illustration {
    flex: 1; width: 100%; margin: 14px 0 10px;
    background: radial-gradient(ellipse at 55% 45%, var(--illustration-b) 0%, var(--illustration-a) 55%, var(--blush) 80%);
    border-radius: 4px;
  }
  .volume { font-size: 8px; letter-spacing: 0.4px; color: var(--rose); white-space: nowrap; }
  .skin-type-foot { font-size: 9px; letter-spacing: 0.6px; color: var(--rose-soft); margin-bottom: 8px; }

  .tube-label   { width: 140px; height: 420px; }
  .bottle-label { width: 120px; height: 450px; }
  .toner-label  { width: 130px; height: 470px; }
  .serum-label  { width: 100px; height: 320px; padding-top: 16px; }
  .jar-label    { width: 150px; height: 170px; padding: 14px 10px 10px; }

  .carton { display: flex; }
  .carton-front { width: 190px; height: 600px; padding-top: 40px; }
  .carton-front .brand-mark { width: 40px; height: 40px; }
  .carton-front .brand-name { font-size: 24px; }
  .carton-front .brand-tagline { font-size: 7px; }
  .carton-front .product-name { font-size: 14px; margin-top: 40px; }
  .carton-front .product-benefit { font-size: 7px; }
  .carton-side {
    width: 56px; background: var(--blush-deep);
    display: flex; flex-direction: column; align-items: center;
    padding-top: 40px;
  }
  .cert-badge {
    width: 30px; height: 30px; border-radius: 50%;
    border: 1px solid var(--rose-soft);
  }
  .side-rule { width: 18px; height: 1px; background: var(--rose-line); margin: 22px 0; }
  .claim-icon { width: 22px; height: 28px; stroke: var(--rose); fill: none; stroke-width: 1.1; }
  .claim-text {
    font-size: 7px; line-height: 1.4; letter-spacing: 0.3px;
    text-transform: uppercase; text-align: center; margin-top: 6px;
    color: var(--rose);
  }

  .night-carton .carton-front { width: 170px; height: 330px; padding-top: 24px; }
  .night-carton .brand-name { font-size: 19px; }
  .night-carton .product-name { margin-top: 26px; font-size: 11px; }
  .night-carton .carton-side { width: 40px; padding-top: 24px; }
  .night-carton .side-rule { margin: 12px 0; width: 14px; }
  .night-carton .claim-icon { width: 16px; height: 20px; }
  .night-carton .claim-text { font-size: 5.5px; }
  .night-carton .cert-badge { width: 22px; height: 22px; }

  .serum-label .brand-name { font-size: 13px; letter-spacing: 1px; }
  .serum-label .brand-tagline { font-size: 5px; letter-spacing: 1px; }
  .serum-label .brand-mark { width: 22px; height: 22px; }
  .serum-label .product-name { font-size: 9.5px; letter-spacing: 1px; margin-top: 16px; white-space: nowrap; }
  .jar-label .brand-mark { display: none; }
  .jar-label .brand-name { font-size: 16px; }
  .jar-label .product-name { margin-top: 12px; font-size: 10px; }
  .jar-label .skin-type { margin-top: 10px; }
  .jar-label .volume { margin-top: 4px; }
</style>
</head>
<body>
<main class="range">

  <section class="label tube-label">
    <div class="brand-mark"></div>
    <div class="brand-name">VELORENA</div>
    <div class="brand-tagline">SKIN IN BALANCE</div>
    <div class="product-name">Gentle<br>Cleanser</div>
    <div class="product-benefit">Deep Cleanse &amp; Refresh</div>
    <div class="skin-type">All Skin Types</div>
    <div class="volume" style="margin-top:8px">100ml ℮ 3.38 fl.oz</div>
    <div class="illustration" role="img" aria-label="Fine-line rose stem illustration"></div>
  </section>

  <section class="label bottle-label">
    <div class="brand-mark"></div>
    <div class="brand-name">VELORENA</div>
    <div class="brand-tagline">SKIN IN BALANCE</div>
    <div class="product-name">Light<br>Moisturising<br>Day Cream</div>
    <div class="product-benefit">Deep Hydration Soft &amp;<br>Glowing Skin</div>
    <div class="divider"></div>
    <div class="product-claim">Tideshift Balance<br>Hydration</div>
    <div class="illustration" role="img" aria-label="Fine-line rose stem illustration"></div>
    <div class="skin-type-foot">All Skin Types</div>
    <div class="volume">50ml ℮ 1.69 fl.oz</div>
  </section>

  <section class="carton hero-carton">
    <div class="label carton-front">
      <div class="brand-mark"></div>
      <div class="brand-name">VELORENA</div>
      <div class="brand-tagline">SKIN IN BALANCE</div>
      <div class="product-name">Light<br>Moisturising<br>Day Cream</div>
      <div class="product-benefit">Deep Hydration Soft &amp;<br>Glowing Skin</div>
      <div class="divider"></div>
      <div class="product-claim">Tideshift Balance<br>Hydration</div>
      <div class="illustration" role="img" aria-label="Fine-line rose stem illustration"></div>
      <div class="skin-type-foot">All Skin Types</div>
      <div class="volume" style="font-size:10px">50ml ℮ 1.69 fl.oz</div>
    </div>
    <aside class="carton-side">
      <div class="cert-badge"></div>
      <div class="side-rule"></div>
      <svg class="claim-icon" viewBox="0 0 22 28"><path d="M11 2 C20 10 20 20 11 26 C2 20 2 10 11 2 Z M11 8 V26"/></svg>
      <div class="claim-text">Vegan<br>Friendly</div>
      <div class="side-rule"></div>
      <svg class="claim-icon" viewBox="0 0 22 28"><path d="M11 4 V26 M11 10 C6 8 5 12 5 14 C8 14 11 13 11 10 M11 10 C16 8 17 12 17 14 C14 14 11 13 11 10 M11 18 C6 16 5 20 5 22 C8 22 11 21 11 18 M11 18 C16 16 17 20 17 22 C14 22 11 21 11 18"/></svg>
      <div class="claim-text">Gluten<br>Free</div>
      <div class="side-rule"></div>
      <svg class="claim-icon" viewBox="0 0 22 28"><path d="M4 12 H18 M5 12 C5 7 17 7 17 12 M6 12 C6 20 11 25 11 25 C11 25 16 20 16 12 M11 7 V4"/></svg>
      <div class="claim-text">Nut<br>Free</div>
    </aside>
  </section>

  <section class="label toner-label">
    <div class="brand-mark"></div>
    <div class="brand-name">VELORENA</div>
    <div class="brand-tagline">SKIN IN BALANCE</div>
    <div class="product-name">Rose<br>Toner</div>
    <div class="product-benefit">Hydrate &amp; Refresh</div>
    <div class="skin-type">All Skin Types</div>
    <div class="illustration" role="img" aria-label="Fine-line rose stem illustration"></div>
    <div class="volume">150ml ℮ 5.07 fl.oz</div>
  </section>

  <section class="label serum-label">
    <div class="brand-mark"></div>
    <div class="brand-name">VELORENA</div>
    <div class="brand-tagline">SKIN IN BALANCE</div>
    <div class="product-name">Glow Serum</div>
    <div class="product-benefit">Brighten &amp; Renew</div>
    <div class="skin-type">All Skin Types</div>
    <div class="volume" style="margin-top:6px">30ml ℮ 1.01 fl.oz</div>
    <div class="illustration" role="img" aria-label="Fine-line rose bloom illustration"></div>
  </section>

  <section class="carton night-carton">
    <div class="label carton-front">
      <div class="brand-mark"></div>
      <div class="brand-name">VELORENA</div>
      <div class="brand-tagline">SKIN IN BALANCE</div>
      <div class="product-name">Night Cream</div>
      <div class="product-benefit">Repair &amp; Nourish</div>
      <div class="skin-type">All Skin Types</div>
      <div class="volume" style="margin-top:8px">50ml ℮ 1.69 fl.oz</div>
      <div class="illustration" role="img" aria-label="Fine-line rose bloom illustration"></div>
    </div>
    <aside class="carton-side">
      <div class="cert-badge"></div>
      <div class="side-rule"></div>
      <svg class="claim-icon" viewBox="0 0 22 28"><path d="M11 2 C20 10 20 20 11 26 C2 20 2 10 11 2 Z M11 8 V26"/></svg>
      <div class="claim-text">Vegan<br>Friendly</div>
      <div class="side-rule"></div>
      <svg class="claim-icon" viewBox="0 0 22 28"><path d="M11 4 V26 M11 10 C6 8 5 12 5 14 C8 14 11 13 11 10 M11 10 C16 8 17 12 17 14 C14 14 11 13 11 10 M11 18 C6 16 5 20 5 22 C8 22 11 21 11 18 M11 18 C16 16 17 20 17 22 C14 22 11 21 11 18"/></svg>
      <div class="claim-text">Gluten<br>Free</div>
      <div class="side-rule"></div>
      <svg class="claim-icon" viewBox="0 0 22 28"><path d="M4 12 H18 M5 12 C5 7 17 7 17 12 M6 12 C6 20 11 25 11 25 C11 25 16 20 16 12 M11 7 V4"/></svg>
      <div class="claim-text">Nut<br>Free</div>
    </aside>
  </section>

  <section class="label jar-label">
    <div class="brand-mark"></div>
    <div class="brand-name">VELORENA</div>
    <div class="brand-tagline">SKIN IN BALANCE</div>
    <div class="product-name">Night Cream</div>
    <div class="product-benefit">Repair &amp; Nourish</div>
    <div class="skin-type">All Skin Types</div>
    <div class="volume">50ml ℮ 1.69 fl.oz</div>
  </section>

</main>
</body>
</html>
```